Website for a mini excavator hire business
Bridgeway Plant Hire
Construction
www.bwphire.com.au
Bridgeway Plant Hire, offers affordable, fully serviced and maintained excavator hire, for long or short term periods.
We have available late model Tarvolen excavator for all your earthmoving needs.
TVL Mini Hydraulic Excavators come equipped with an aluminium trailer and 3 buckets as standard.
Perfect for builders, plumbers, electrical contractors and landscape gardeners.
Would like a modern masculine website that is simple and easy to read and navigate for our customers who are tradesman. I like the silhouette of excavators in the header image.
below header
www.kestrelhaulage.com.au
www.brannockrent.com.au
www.trenchpilot.net.au/home
Looking for a modern and crisp website design that is masculine in style and color.
Some text from the back of my business card that could be used on the front page of the website.
Regards,
Dorian Pelkaw.

```html
<!DOCTYPE html>
<html lang="en">
<head>
<meta charset="utf-8">
<title>Bridgeway Plant Hire</title>
<link rel="stylesheet" href="https://fonts.googleapis.com/css2?family=Arimo:wght@400;700&display=swap">
<style>
:root{
  --yellow:#f5d90a;
  --yellow-dark:#d9b800;
  --black:#0b0b0b;
  --ink:#141414;
  --grey:#8a8a8a;
  --white:#ffffff;
  --text:#e6e6e6;
}
*{margin:0;padding:0;box-sizing:border-box}
html,body{width:1200px;height:696px;overflow:hidden;background:var(--black)}
body{font-family:"Arimo",Arial,sans-serif;color:var(--white);position:relative}
.header{position:absolute;left:0;top:0;width:1200px;height:204px;background:#050505}
.header-scene{position:absolute;left:430px;top:0;width:770px;height:204px;
  background:linear-gradient(90deg,#050505 0%,#3a3a3a 25%,#9a9a9a 60%,#c9c9c9 80%,#8f8f8f 100%)}
.brand{position:absolute;left:137px;top:48px;display:flex;align-items:center;gap:18px}
.brand-square{width:104px;height:112px;background:var(--yellow)}
.brand-text{display:flex;flex-direction:column;gap:10px}
.brand-name{font-weight:700;font-size:36px;line-height:1;color:var(--yellow);white-space:nowrap}
.brand-tagline{font-weight:700;font-size:17px;color:var(--white);white-space:nowrap}
.phone-tab{position:absolute;left:864px;top:0;width:196px;height:42px;background:var(--yellow);
  border-radius:0 0 10px 10px;display:flex;align-items:center;justify-content:center;gap:10px;
  font-weight:700;font-size:17px;color:var(--ink)}
.nav{position:absolute;left:0;top:204px;width:1200px;height:60px;
  background:linear-gradient(#cfcfcf,#8c8c8c);display:flex;align-items:center;padding-left:120px}
.nav a{display:block;padding:0 19px;height:60px;line-height:60px;font-size:14px;font-weight:700;
  color:var(--ink);text-decoration:none;border-right:1px solid #6f6f6f;white-space:nowrap}
.nav a.active{color:var(--yellow)}
.nav a.last{border-right:none}
.search{position:absolute;left:754px;top:9px;width:340px;height:42px;border-radius:4px;
  background:linear-gradient(#555,#7a7a7a);border:1px solid #4a4a4a}
.search svg{position:absolute;right:14px;top:12px}
.main{position:absolute;left:0;top:264px;width:1200px;height:348px;
  background:linear-gradient(#111 0%,#1e1e1e 100%)}
.photo-frame{position:absolute;left:132px;top:24px;width:344px;height:276px;background:var(--white);padding:12px}
.photo{width:100%;height:100%;background:radial-gradient(circle at 50% 55%,#e3c21a 0%,#8a7a2a 45%,#f2f2f2 80%)}
.content{position:absolute;left:511px;top:34px;width:570px}
.welcome{font-weight:700;font-size:18px;color:var(--white);display:flex;align-items:center;gap:10px;white-space:nowrap}
.welcome span{color:var(--yellow)}
.welcome::after{content:"";flex:1;height:2px;background:var(--yellow)}
.specialist{margin-top:14px;padding-bottom:6px;border-bottom:1px solid #444;font-weight:700;font-size:15px;color:var(--yellow)}
.about{margin-top:6px;font-size:12.5px;line-height:16.5px;color:var(--text)}
.price{position:absolute;left:511px;top:245px;width:560px;height:55px}
.price svg{position:absolute;left:0;top:0}
.price-label{position:absolute;left:20px;top:0;height:55px;line-height:55px;font-size:13.5px;color:var(--ink);white-space:nowrap}
.price-label strong{font-size:17px}
.footer{position:absolute;left:0;top:612px;width:1200px;height:84px;background:#111;
  display:flex;align-items:center;justify-content:center;gap:26px;font-size:14px;color:var(--white)}
.footer .name{color:var(--yellow)}
</style>
</head>
<body>
<header class="header">
  <div class="header-scene" role="img" aria-label="Silhouettes of excavators and a dump truck against a grey sky"></div>
  <div class="brand">
    <div class="brand-square"></div>
    <div class="brand-text">
      <div class="brand-name">Bridgeway Plant Hire</div>
      <div class="brand-tagline">Get the job done for less</div>
    </div>
  </div>
  <div class="phone-tab">
    <svg width="22" height="22" viewBox="0 0 22 22"><circle cx="11" cy="11" r="10" fill="var(--ink)"/><path d="M7.5 6.5l2 0 1 2.5-1.3 1a6 6 0 0 0 3 3l1-1.3 2.5 1v2a1 1 0 0 1-1 1A8.5 8.5 0 0 1 6.5 7.5a1 1 0 0 1 1-1z" fill="var(--yellow)"/></svg>
    1300 - 47 - 62 - 90
  </div>
</header>
<nav class="nav">
  <a class="active" href="#">HOME</a>
  <a href="#">ABOUT US</a>
  <a href="#">OUR EQUIPMENT</a>
  <a href="#">SAFETY</a>
  <a class="last" href="#">CONTACT US</a>
  <div class="search">
    <svg width="16" height="16" viewBox="0 0 16 16"><circle cx="6.5" cy="6.5" r="4.5" fill="none" stroke="#fff" stroke-width="2"/><path d="M10 10l4 4" stroke="#fff" stroke-width="2"/></svg>
  </div>
</nav>
<main class="main">
  <div class="photo-frame"><div class="photo" role="img" aria-label="Yellow wheel loader photographed on a white background"></div></div>
  <section class="content">
    <h1 class="welcome">WELCOME TO <span>BRIDGEWAY PLANT HIRE</span></h1>
    <h2 class="specialist">WE ARE MELBOURNE'S MINI EXCAVATOR SPECIALIST</h2>
    <p class="about">Bridgeway Plant Hire, based in Melbourne's North-Eastern suburbs offers affordable, fully serviced and maintained excavator hire, for long or short term periods.<br>
    We have available late model Tarvolen excavators featuring buckets and augers for all your earthmoving needs.<br>
    TVL Mini Hydraulic Excavators come equipped with an aluminium trailer and 3 buckets as standard. Auger attachments are also available.<br>
    Perfect for builders, plumbers, electrical contractors and landscape gardeners.</p>
  </section>
  <div class="price">
    <svg width="560" height="55" viewBox="0 0 560 55"><path d="M0 0H535L560 27.5 535 55H0Z" fill="var(--yellow)"/><path d="M0 52H536L534.5 55H0Z" fill="var(--yellow-dark)"/></svg>
    <div class="price-label">PRICE STARTING AT <strong>$297</strong> PER DAY (INCLUDES 3 BUCKETS, TRAILERS &amp; GST)</div>
  </div>
</main>
<footer class="footer">
  <span>Copyright © 2013 <span class="name">Bridgeway Plant</span></span>
  <span>|</span><span>Privacy policy</span><span>|</span><span>Terms &amp; Conditions Applied</span>
</footer>
</body>
</html>
```